Brisk Hollow Builders Needs A Flyer

We need a flyer for our newest product "The Cedarlane Garden Workroom"

Here is some copy for the flyer:

1. More and more people everyday are working from home and finding it difficult to disconnect from home activities in order to focus on their work. They are also finding it very expensive to add on to their existing house for a quiet place. Our archatectually stunning, Cedarlane Garden Workroom is the answer. The office studio measures 16' wide and 10' deep. 160 Square feet of space.

Perfect for dozens of purposes. Home office, design studio, artist studio, home school office, reading room, craft studio, drafting room.

Features include:

- Steel Framing. 40-60% lighter then wood, higher strength to weight ratio, resistant to mold and fire and steel is the most recycled material on earth!
- Spray foam insulation. Cool in the summer and warm in the winter.
- HVAC Mini Split with wireless remote control and thermostat.
- 100% Off grid with enough solar and battery storage to run your entire office. No need to pay for an expensive electric installation.
- Flush fitting floor outlets to reduce wires.
- TV mount (Optional with pre-wired electric, HDMI, digital audio & Cat 6)
- Windows are tempered glass custom made by Morvik Glazing.
- Solar qualifies for a 26% tax credit. This is not a write-off rather it is a direct reduction on your tax obligation.
- Thousands of dollars less than adding onto your home.
- Custom color, siding, features available.

This beautiful back yard office is delivered 100% assembled and ready to enjoy on the day of delivery.

We ship nationwide from our factory in South Carolina. Give us a call anytime to speak to a designer and start your dream office today!

555-318-4027
info@BriskHollowBuilders.example

```html
<!DOCTYPE html>
<html lang="en">
<head>
<meta charset="utf-8">
<title>Cedarlane Garden Workroom Flyer</title>
<link href="https://fonts.googleapis.com/css2?family=Montserrat:wght@400;500;600;700;800;900&display=swap" rel="stylesheet">
<style>
:root{
  --orange:#f0901e;
  --green:#1d4a22;
  --ink:#161616;
  --panel:#e4e4e6;
  --paper:#ffffff;
  --backdrop:#e8e5de;
}
*{box-sizing:border-box;margin:0;padding:0}
html,body{width:1200px;height:900px;overflow:hidden;background:var(--backdrop);font-family:'Montserrat',sans-serif}
.flyer{position:absolute;left:296px;top:20px;width:608px;height:860px;background:var(--paper);overflow:hidden;box-shadow:0 6px 20px rgba(0,0,0,.12)}
.ship-band{position:absolute;left:0;top:0;width:440px;height:34px;background:var(--orange);color:#fff;font-weight:800;font-size:8.5px;letter-spacing:1.4px;white-space:nowrap;display:flex;align-items:center;padding-left:16px}
.hero-photo{position:absolute;left:0;top:34px;width:608px;height:280px;background:linear-gradient(170deg,#9ab4c7 0%,#6f8a62 35%,#3d4a3a 60%,#5d7046 85%,#3f5a2c 100%)}
.brand-box{position:absolute;right:0;top:0;width:168px;height:92px;background:var(--paper);border-bottom-left-radius:34px;display:flex;align-items:center;justify-content:center;gap:6px;padding:0 10px}
.brand-dot{width:12px;height:12px;border-radius:50%;background:var(--orange);flex:none}
.brand-name{font-weight:800;font-size:15px;line-height:1.05;color:var(--orange);text-transform:uppercase}
.title-band{position:absolute;left:0;top:304px;width:608px;height:112px;background:var(--green);display:flex;align-items:center}
.title{width:332px;padding-left:24px;color:#fff;font-weight:900;font-size:29px;line-height:1.05;text-transform:uppercase}
.title-divider{width:2px;height:74px;background:var(--orange);margin-right:16px}
.purposes{flex:1;color:#fff;font-size:10px;font-weight:500;line-height:1.35;text-transform:uppercase;padding-right:20px}
.features-tab{position:absolute;left:26px;top:416px;width:44px;height:310px;background:var(--orange);border-bottom-left-radius:22px;border-bottom-right-radius:22px;display:flex;align-items:center;justify-content:center}
.features-tab span{transform:rotate(-90deg);white-space:nowrap;color:#fff;font-weight:800;font-size:19px;letter-spacing:2px}
.feature-list{position:absolute;left:84px;top:426px;width:260px;list-style:none;font-size:10.2px;line-height:1.3;color:var(--ink)}
.feature-list li{position:relative;padding-left:15px;margin-bottom:1.5px}
.feature-list li::before{content:"";position:absolute;left:0;top:2px;width:10px;height:10px;background:var(--orange);border-radius:1px}
.feature-list li::after{content:"";position:absolute;left:3.5px;top:3px;width:3px;height:6px;border:solid #fff;border-width:0 1.6px 1.6px 0;transform:rotate(45deg)}
.story-panel{position:absolute;left:352px;top:416px;width:256px;height:172px;background:var(--panel);border-bottom-left-radius:90px;padding:14px 18px 0 22px;font-size:10px;line-height:1.35;color:var(--ink);text-align:center}
.render-photo{position:absolute;left:376px;top:596px;width:200px;height:92px;background:linear-gradient(160deg,#d9d6d0,#3a3c3f 60%,#2a2b2d)}
.frame-drawing{position:absolute;left:440px;top:694px;width:150px;height:40px;background:linear-gradient(90deg,#cfcfcf,#9a9a9a)}
.delivery-box{position:absolute;left:36px;top:748px;width:380px;border:3px solid var(--green);padding:5px 12px;font-size:13px;line-height:1.3;color:var(--ink)}
.contact-band{position:absolute;left:0;top:818px;width:608px;height:42px;background:var(--ink);padding:5px 0 0 30px;color:#fff}
.contact-line{display:flex;align-items:center;gap:14px;font-size:13px}
.contact-line .phone{font-weight:800;display:flex;align-items:center;gap:5px}
.contact-line .email{display:flex;align-items:center;gap:5px;font-weight:500}
.contact-cta{color:var(--orange);font-weight:800;font-size:8.5px;letter-spacing:1.6px;margin-top:3px;text-transform:uppercase}
.call-corner{position:absolute;left:430px;top:738px;width:178px;height:122px;background:var(--orange);border-top-left-radius:70px;display:flex;align-items:center;justify-content:center;text-align:center}
.call-corner span{font-weight:900;font-size:19px;line-height:1.05;color:var(--ink);text-transform:uppercase}
</style>
</head>
<body>
<main class="flyer">
  <div class="hero-photo" role="img" aria-label="Photo of a dark-clad garden studio with large glazed front set in a landscaped back yard"></div>
  <div class="ship-band">WE SHIP NATIONWIDE FROM OUR FACTORY IN SOUTH CAROLINA</div>
  <div class="brand-box"><span class="brand-dot"></span><span class="brand-name">Brisk Hollow Builders</span></div>

  <section class="title-band">
    <h1 class="title">Cedarlane Garden Workroom</h1>
    <div class="title-divider"></div>
    <p class="purposes">Perfect for dozens of purposes. Home office, design studio, artist studio, home school office, reading room, craft studio, drafting room.</p>
  </section>

  <div class="features-tab"><span>FEATURES INCLUDED</span></div>
  <ul class="feature-list">
    <li>Steel Framing. 40-60% lighter then wood, higher strength to weight ratio, resistant to mold and fire and steel is the most recycled material on earth!</li>
    <li>Spray foam insulation. Cool in the summer and warm in the winter.</li>
    <li>HVAC Mini Split with wireless remote control and thermostat.</li>
    <li>100% Off grid with enough solar and battery storage to run your entire office. No need to pay for an expensive electric installation.</li>
    <li>Flush fitting floor outlets to reduce wires.</li>
    <li>TV mount (Optional with pre-wired electric, HDMI, digital audio &amp; Cat 6)</li>
    <li>Windows are tempered glass custom made by Morvik Glazing.</li>
    <li>Solar qualifies for a 26% tax credit. This is not a write-off rather it is a direct reduction on your tax obligation.</li>
    <li>Thousands of dollars less than adding onto your home.</li>
    <li>Custom color, siding, features available.</li>
  </ul>

  <p class="story-panel">More and more people everyday are working from home and finding it difficult to disconnect from home activities in order to focus on their work. They are also finding it very expensive to add on to their existing house for a quiet place. Our archatectually stunning, Cedarlane Garden Workroom is the answer. The office studio measures 16' wide and 10' deep. 160 Square feet of space.</p>

  <div class="render-photo" role="img" aria-label="Rendering of the garden workroom seen from the front corner"></div>
  <div class="frame-drawing" role="img" aria-label="Exploded drawing of the steel frame panels"></div>

  <p class="delivery-box">This beautiful back yard office is delivered 100% assembled and ready to enjoy on the day of delivery.</p>

  <div class="call-corner"><span>Give us a<br>call anytime</span></div>

  <footer class="contact-band">
    <div class="contact-line">
      <span class="phone"><svg width="11" height="11" viewBox="0 0 24 24"><path fill="#f0901e" d="M6.6 10.8a15 15 0 0 0 6.6 6.6l2.2-2.2a1 1 0 0 1 1-.25 11.4 11.4 0 0 0 3.6.57 1 1 0 0 1 1 1V20a1 1 0 0 1-1 1A17 17 0 0 1 3 4a1 1 0 0 1 1-1h3.5a1 1 0 0 1 1 1c0 1.25.2 2.45.57 3.6a1 1 0 0 1-.25 1z"/></svg>555-318-4027</span>
      <span class="email"><svg width="12" height="10" viewBox="0 0 24 18"><rect x="1" y="1" width="22" height="16" rx="2" fill="none" stroke="#f0901e" stroke-width="2"/><path d="M1 2l11 8 11-8" fill="none" stroke="#f0901e" stroke-width="2"/></svg>info@BriskHollowBuilders.example</span>
    </div>
    <p class="contact-cta">Speak to a designer and start your dream office today!</p>
  </footer>
</main>
</body>
</html>
```